Motorcycle Tours Facebook Page

Wanting a fresh design for a Motorcycle Tour company running tours in Far North Queensland. Our market is city people who cant ride their own bikes that far and we look after them by picking them up at the airport, taking care of evrything, giving them a bike and gear and as a small group go riding through amazing secenery on great roads. We stop at rainforests, worl heritage sites and just enjoy a couple of days riding. We expect our audience may be all ages but probably over 40's. We want to express fun, enjoyment, good company, great food, amazing scenery. Have uploaded logo and a couple of images.

```html
<!DOCTYPE html>
<html lang="en">
<head>
<meta charset="utf-8">
<title>Coastline Rides – Facebook Cover</title>
<link href="https://fonts.googleapis.com/css2?family=Oswald:wght@400;500&family=Roboto:wght@400&display=swap" rel="stylesheet">
<style>
  :root {
    --stage: #363636;
    --orange-light: #f27a3e;
    --orange-deep: #e0541c;
    --teal: #3cc3c8;
    --white: #ffffff;
    --ink: #333333;
  }
  * { margin: 0; padding: 0; box-sizing: border-box; }
  html, body {
    width: 1200px; height: 1200px; overflow: hidden;
    background: var(--stage);
  }
  .cover {
    position: absolute; left: 0; top: 373px;
    width: 1200px; height: 453px; overflow: hidden;
  }
  .cover-art, .headline { position: absolute; inset: 0; }
  .headline text {
    font-family: 'Oswald', sans-serif; fill: var(--white);
  }
  .headline-lead { font-size: 54px; font-weight: 400; }
  .headline-main { font-size: 134px; font-weight: 500; }
  .call-box {
    position: absolute; left: 750px; top: 311px;
    width: 381px; height: 49px; background: var(--white);
    display: flex; align-items: center; justify-content: center; gap: 10px;
    font-family: 'Roboto', sans-serif; font-size: 21px; color: var(--ink);
  }
  .call-box svg { width: 28px; height: 28px; }
  .brand-name {
    position: absolute; left: 14px; bottom: 14px;
    display: flex; align-items: center; gap: 8px;
    font-family: 'Oswald', sans-serif; font-weight: 500; font-size: 26px;
    color: var(--orange-deep);
  }
  .brand-name .dot {
    width: 16px; height: 16px; border-radius: 50%; background: var(--orange-deep);
  }
</style>
</head>
<body>
  <section class="cover">
    <svg class="cover-art" viewBox="0 0 1200 453" width="1200" height="453">
      <defs>
        <linearGradient id="coast" x1="0" y1="0" x2="1" y2="0.3">
          <stop offset="0" stop-color="#5f7b3e"/>
          <stop offset="0.45" stop-color="#8a8f5a"/>
          <stop offset="0.62" stop-color="#4fc0c2"/>
          <stop offset="1" stop-color="#3fb6c0"/>
        </linearGradient>
        <linearGradient id="panel" x1="0" y1="0" x2="0" y2="1">
          <stop offset="0" stop-color="#f27a3e"/>
          <stop offset="1" stop-color="#e0541c"/>
        </linearGradient>
        <linearGradient id="shot-a" x1="0" y1="0" x2="0" y2="1">
          <stop offset="0" stop-color="#c9c9c4"/><stop offset="1" stop-color="#4a3a38"/>
        </linearGradient>
        <linearGradient id="shot-b" x1="0" y1="0" x2="0" y2="1">
          <stop offset="0" stop-color="#4e5a3c"/><stop offset="1" stop-color="#7a7a78"/>
        </linearGradient>
        <linearGradient id="shot-c" x1="0" y1="0" x2="0" y2="1">
          <stop offset="0" stop-color="#8ca05a"/><stop offset="1" stop-color="#5e6a3c"/>
        </linearGradient>
      </defs>

      <rect class="coast-photo" role="img" aria-label="Aerial photo of a winding coastal road above a turquoise river mouth and forested hills" x="0" y="0" width="760" height="453" fill="url(#coast)"/>

      <polygon class="panel-edge" points="694,0 1200,0 1200,453 629,453" fill="#3cc3c8"/>
      <polygon class="panel" points="702,0 1200,0 1200,453 637,453" fill="url(#panel)"/>

      <g class="photo-chain" stroke="#3cc3c8" stroke-width="8" fill="none">
        <line x1="625" y1="136" x2="629" y2="161"/>
        <line x1="629" y1="289" x2="646" y2="310"/>
      </g>

      <g class="photo-badge">
        <circle cx="625" cy="72" r="66" fill="#fff"/>
        <circle cx="625" cy="72" r="62" fill="#e0541c"/>
        <circle role="img" aria-label="Photo of a touring motorcycle parked outside a roadside café" cx="625" cy="72" r="58" fill="url(#shot-a)"/>
      </g>
      <g class="photo-badge">
        <circle cx="629" cy="225" r="66" fill="#fff"/>
        <circle cx="629" cy="225" r="62" fill="#e0541c"/>
        <circle role="img" aria-label="Photo of a rider leaning into a bend on a mountain road" cx="629" cy="225" r="58" fill="url(#shot-b)"/>
      </g>
      <g class="photo-badge">
        <circle cx="646" cy="374" r="66" fill="#fff"/>
        <circle cx="646" cy="374" r="62" fill="#e0541c"/>
        <circle role="img" aria-label="Photo of a shaded rainforest walking path" cx="646" cy="374" r="58" fill="url(#shot-c)"/>
      </g>
    </svg>

    <svg class="headline" viewBox="0 0 1200 453" width="1200" height="453">
      <text class="headline-lead" x="746" y="171" textLength="394" lengthAdjust="spacingAndGlyphs">PLAN YOUR AMAZING</text>
      <text class="headline-main" x="743" y="290" textLength="403" lengthAdjust="spacingAndGlyphs">HOLIDAY</text>
    </svg>

    <div class="call-box">
      <svg viewBox="0 0 28 28" aria-hidden="true">
        <circle cx="14" cy="14" r="12.5" fill="none" stroke="#333" stroke-width="1.6"/>
        <path d="M9.5 8.5c.8-.8 1.6-.6 2 .1l1.2 2c.3.6.1 1.2-.4 1.6l-.7.5c.6 1.4 1.7 2.6 3.1 3.2l.5-.7c.4-.5 1-.7 1.6-.4l2 1.2c.7.4.9 1.2.1 2-1.6 1.6-4.2.9-6.6-1.5S7.9 10.1 9.5 8.5z" fill="#333"/>
      </svg>
      <span>CALL US : 800-555-010-2040</span>
    </div>

    <div class="brand-name"><span class="dot"></span>Coastline Rides</div>
  </section>
</body>
</html>
```